Pale Ridge Software

We are a software company selling endpoint visibility, access and security technology to enterprise-level IT departments.

Our technology helps organizations gain comprehensive visibility into and control over devices accessing their corporate network so they can quickly identify and address suspicious activity on the network that could lead to potential threats like data breaches.

This technology can cost organizations upwards of $1M - depending on the size of the organization. Our primary clients are Summit 3,000 companies.

We want a professional, polished business card to represent our new brand.

Info fields to include on the card:
Name
Job Title
Office Phone #
Cell Phone #
Email address
Address: 4172 Wexmoor Pond Ave., Ste. 2600, Larkfield, MN 55819
Website address: www.paleridgesoftware.example
Tagline: Reveal every device. Secure the network.

Logo files and color specs document are attached. Would like color scheme to coordinate with the logo.

Also looking at stationary/envelope designs in conjunction with the business card designs. Received very few designs that included the stationary.

```html
<!DOCTYPE html>
<html lang="en">
<head>
<meta charset="utf-8">
<title>Pale Ridge Software – Business Card</title>
<link href="https://fonts.googleapis.com/css2?family=Montserrat:wght@400;500;600;700&display=swap" rel="stylesheet">
<style>
  :root {
    --backdrop: #2b2b2d;
    --brand-red: #8f141c;
    --brand-red-deep: #7a1017;
    --brand-orange: #c9703f;
    --card-white: #f6f6f6;
    --ink: #4a4a4a;
    --ink-soft: #6b6b6b;
    --label-red: #9b2a2f;
  }
  * { box-sizing: border-box; margin: 0; padding: 0; }
  html, body { width: 1200px; height: 900px; overflow: hidden; }
  body {
    background: var(--backdrop);
    font-family: "Montserrat", sans-serif;
    display: flex;
    flex-direction: column;
    align-items: center;
    justify-content: center;
    gap: 50px;
  }
  .card {
    width: 640px;
    height: 366px;
    border-radius: 26px;
    position: relative;
    overflow: hidden;
    box-shadow: 0 14px 30px rgba(0,0,0,0.45);
  }

  .brand {
    display: flex;
    align-items: center;
    gap: 14px;
  }
  .brand-mark {
    flex: none;
    border-radius: 50%;
  }
  .brand-name {
    font-weight: 600;
    text-transform: uppercase;
    line-height: 1;
    white-space: nowrap;
  }

  /* Back of card */
  .card-back {
    background: linear-gradient(135deg, var(--brand-red) 0%, var(--brand-red-deep) 100%);
    color: #fff;
    display: flex;
    flex-direction: column;
    align-items: center;
    justify-content: center;
    gap: 34px;
  }
  .card-back .brand-mark { background: var(--brand-orange); width: 22px; height: 22px; }
  .card-back .brand-name { font-size: 26px; letter-spacing: 0.2em; color: #fff; }
  .tagline {
    font-size: 14px;
    font-weight: 400;
    letter-spacing: 0.04em;
    color: #f3dcdc;
  }

  /* Front of card */
  .card-front {
    background: linear-gradient(160deg, #ffffff 0%, var(--card-white) 55%, #e8e8e8 100%);
    color: var(--ink);
    padding: 44px 48px;
  }
  .card-front .brand { width: 340px; }
  .card-front .brand-mark { background: var(--brand-red); width: 18px; height: 18px; }
  .card-front .brand-name { font-size: 18px; letter-spacing: 0.14em; color: var(--brand-red); }
  .address {
    position: absolute;
    top: 40px;
    right: 48px;
    width: 170px;
    font-size: 11.5px;
    font-style: normal;
    line-height: 1.5;
    color: var(--ink-soft);
  }
  .texture {
    position: absolute;
    right: 0;
    top: 100px;
    width: 210px;
    height: 266px;
    background: radial-gradient(circle at 70% 55%, rgba(200,200,200,0.55) 0%, rgba(230,230,230,0) 70%);
  }
  .person { margin-top: 74px; position: relative; }
  .person-name {
    font-size: 20px;
    font-weight: 600;
    color: var(--brand-red);
    letter-spacing: 0.03em;
    text-transform: uppercase;
  }
  .person-title {
    font-size: 13px;
    font-weight: 600;
    color: var(--ink);
    margin-top: 4px;
  }
  .contact {
    margin-top: 22px;
    display: grid;
    grid-template-columns: 64px auto;
    row-gap: 3px;
    font-size: 15px;
  }
  .contact dt { color: var(--label-red); font-weight: 500; }
  .contact dd { color: var(--ink); }
</style>
</head>
<body>
  <section class="card card-back">
    <div class="brand">
      <span class="brand-mark"></span>
      <span class="brand-name">Pale Ridge Software</span>
    </div>
    <p class="tagline">Reveal every device. Secure the network.</p>
  </section>

  <section class="card card-front">
    <div class="texture" role="img" aria-label="Faint grey decorative circle pattern"></div>
    <div class="brand">
      <span class="brand-mark"></span>
      <span class="brand-name">Pale Ridge Software</span>
    </div>
    <address class="address">
      4172 Wexmoor Pond Ave.<br>
      Ste. 2600, Larkfield<br>
      MN 55819
    </address>
    <div class="person">
      <h1 class="person-name">Marcus Hollenby</h1>
      <p class="person-title">Managing Director</p>
      <dl class="contact">
        <dt>Office:</dt><dd>5555 555 555</dd>
        <dt>Cell:</dt><dd>5555 555 555</dd>
        <dt>Email:</dt><dd>mhollenby@paleridgesoftware.example</dd>
        <dt>Web:</dt><dd>www.paleridgesoftware.example</dd>
      </dl>
    </div>
  </section>
</body>
</html>
```